Bridgeway, Lantern, and the Quiet Harbor Loop Research Program Website

Overview: This website will serve a new research program (Bridgeway, Lantern, and the Quiet Harbor Loop) at the Fenmoor University School of Medicine. I want a clean, intuitive design that has a navigation bar, but uses icons/graphic buttons to link to the main pages. In an attached Word document, I have provided a basic information architecture for the site, understanding that this project would just generate graphics and code for the 3 pages. I highlighted the 3 pages I'd like designed.
Target market: People who want to participate in our research, or contribute grant funding to specific projects.
Number of page: The design project focuses on 3 pages, but the site must accommodate 6 pages with top-level links. See attached Word doc.
Logo and website header: Please integrate our logo in the header. I've uploaded it as a png file--both with the name of the website and with just the logo image. I imaging the logo would look great in a banner set against an image of a mountain. The two main design themes I want to see included are nature and healthcare.
Text content: I have not yet provided text. Use some dummy text.
Technical Specifications:
- Build using WordPress. We will host this site ourselves on Brimloft using WordPress.
- The design package must be coded.
- The template must be responsive to different platforms (e.g., computer, mobile phone, iPad).
Thank you! I look forward to seeing your designs.
- Ned

```html
<!DOCTYPE html>
<html lang="en">
<head>
<meta charset="utf-8">
<title>Bridgeway, Lantern, and the Quiet Harbor Loop – The Research Program</title>
<link rel="stylesheet" href="https://fonts.googleapis.com/css2?family=Baloo+2:wght@700&family=Lato:wght@400;700&family=Poppins:wght@400;700&display=swap">
<style>
:root{
  --navy:#1b5a94;
  --blue:#2a6aa5;
  --blue-bright:#2f7cc4;
  --teal:#3a8a78;
  --green:#7aa932;
  --green-light:#8db543;
  --lime:#a3c93a;
  --text:#555;
  --white:#fff;
  --dark:#111;
}
*{margin:0;padding:0;box-sizing:border-box}
html,body{width:1200px;height:2486px;overflow:hidden;background:var(--white)}
body{position:relative;font-family:'Lato',sans-serif;color:var(--text)}
.abs{position:absolute}

/* header */
.site-header{position:absolute;top:0;left:0;width:1200px;height:78px;background:var(--white);z-index:5}
.brand{position:absolute;left:110px;top:18px;display:flex;align-items:center;gap:10px}
.brand-dot{width:40px;height:40px;border-radius:50%;background:var(--green)}
.brand-name{font-family:'Baloo 2',sans-serif;font-weight:700;font-size:12px;line-height:13px;color:var(--navy);border-left:1px solid var(--navy);padding-left:8px}
.main-nav{position:absolute;right:113px;top:31px;display:flex;gap:31px}
.main-nav a{font-size:15px;color:var(--navy);text-decoration:none;letter-spacing:.2px}

/* hero */
.hero{position:absolute;top:78px;left:0;width:1200px;height:680px;
  background:linear-gradient(180deg,#c8d3dc 0%,#8aa0ad 16%,#5f7a54 30%,#4f8a3a 45%,#2fa9b0 58%,#6fb43c 72%,#8cc43f 100%)}
.hero-mark{position:absolute;left:205px;top:255px;width:140px;height:140px;border-radius:50%;border:4px solid var(--white)}
.hero-rule{position:absolute;left:374px;top:265px;width:2px;height:116px;background:var(--white)}
.hero-title{position:absolute;left:394px;top:278px;font-family:'Baloo 2',sans-serif;font-weight:700;color:var(--white);font-size:34px;line-height:38px;text-shadow:0 2px 4px rgba(0,0,0,.35)}
.hero-sub{position:absolute;left:394px;top:318px;font-family:'Baloo 2',sans-serif;font-weight:700;color:var(--white);font-size:28px;line-height:32px;text-shadow:0 2px 4px rgba(0,0,0,.35)}
.btn{position:absolute;display:flex;align-items:center;justify-content:center;background:var(--green);color:var(--white);font-size:17px;border-radius:24px;text-decoration:none}
.hero .btn{left:505px;top:313px;width:190px;height:46px}

/* venn */
.venn-circle{position:absolute;border-radius:50%;width:292px;height:292px}
.venn-circle::after{content:"";position:absolute;inset:10px;border-radius:50%;border:2px dotted rgba(255,255,255,.85)}
.c-health{left:205px;top:760px;background:var(--teal)}
.c-spirit{left:100px;top:930px;background:rgba(141,181,67,.92)}
.c-values{left:317px;top:935px;background:rgba(42,106,165,.93)}
.venn-label{position:absolute;width:200px;text-align:center;color:var(--white);font-weight:700;font-size:22px}
.venn-icon{position:absolute}

/* vision */
.vision-title{position:absolute;left:681px;top:850px;font-family:'Poppins',sans-serif;font-size:44px;color:var(--navy);font-weight:400}
.vision-title b{font-weight:700}
.vision-text{position:absolute;left:681px;top:932px;width:420px;font-size:15px;line-height:25.7px;color:var(--text)}
.vision .btn{left:681px;top:1124px;width:174px;height:47px}

/* program */
.program{position:absolute;top:1290px;left:0;width:1200px;height:720px;
  background:radial-gradient(ellipse at 30% 40%,#86b33c 0%,#6fa12c 55%,#5f9425 100%)}
.program-mark{position:absolute;left:588px;top:1392px;width:24px;height:24px;border-radius:50%;border:2px solid var(--white)}
.program-title{position:absolute;top:1424px;left:0;width:1200px;text-align:center;font-family:'Poppins',sans-serif;font-size:44px;color:var(--white)}
.program-title b{font-weight:700}
.card{position:absolute;top:1510px;width:311px;height:291px;background:var(--white)}
.card-photo{height:235px}
.card-label{height:56px;display:flex;align-items:center;justify-content:center;font-size:23px;font-weight:700;color:var(--dark)}
.photo-people{background:linear-gradient(180deg,#1f5fb0 0%,#6aa0d8 30%,#c7d43a 62%,#8ab83a 100%)}
.photo-projects{background:linear-gradient(160deg,#8a6a4a 0%,#3f7fd0 30%,#5d93da 60%,#a9c6ea 100%)}
.photo-faqs{background:linear-gradient(180deg,#d98a4a 0%,#e9b070 40%,#6b4a3a 70%,#5b5a5e 100%)}

/* footer */
.site-footer{position:absolute;top:1930px;left:0;width:1200px;height:556px;
  background:linear-gradient(180deg,#2a6cab 0%,#2d6aa3 45%,#23609a 100%)}
.footer-mark{position:absolute;left:370px;top:2015px;width:84px;height:84px;border-radius:50%;border:3px solid var(--white)}
.footer-rule{position:absolute;left:470px;top:2025px;width:2px;height:64px;background:var(--white)}
.footer-brand{position:absolute;left:483px;top:2030px;font-family:'Baloo 2',sans-serif;font-weight:700;color:var(--white);font-size:18px;line-height:20px}
.footer-h{position:absolute;top:2130px;font-family:'Lato',sans-serif;font-weight:700;font-size:30px;color:var(--white)}
.quick-links{position:absolute;left:112px;top:2188px;list-style:none}
.quick-links li{display:flex;align-items:center;gap:20px;height:34.3px;font-size:14px;color:var(--white)}
.contact-list{position:absolute;left:390px;top:2190px;list-style:none;color:var(--white);font-size:14.5px;line-height:20.5px}
.contact-list li{display:flex;gap:22px;margin-bottom:22px}
.contact-list svg{flex:none;margin-top:2px}
.newsletter-text{position:absolute;left:799px;top:2185px;width:240px;font-size:16px;line-height:29px;color:var(--white)}
.email-field{position:absolute;left:799px;top:2266px;width:289px;height:45px;background:var(--white);border-radius:3px;font-size:12px;color:#333;padding:14px 18px}
.submit{position:absolute;left:799px;top:2325px;width:103px;height:40px;border-radius:20px;background:var(--lime);color:var(--white);display:flex;align-items:center;justify-content:center;font-size:16px}
.footer-divider{position:absolute;left:110px;top:2411px;width:980px;height:1px;background:rgba(255,255,255,.25)}
.copyright{position:absolute;top:2432px;left:0;width:1200px;text-align:center;color:var(--white);font-size:16px}
</style>
</head>
<body>

<header class="site-header">
  <div class="brand">
    <span class="brand-dot"></span>
    <span class="brand-name">Bridgeway, Lantern, and the Quiet Harbor Loop<br>The Research Program</span>
  </div>
  <nav class="main-nav">
    <a href="#">HOME</a><a href="#">PEOPLE</a><a href="#">PROJECTS</a><a href="#">FAQS</a><a href="#">RESOURCES</a><a href="#">CONTACT</a>
  </nav>
</header>

<section class="hero" role="img" aria-label="Mountain valley with a turquoise lake, river and green forested slopes">
  <div class="hero-mark" style="top:177px"></div>
  <div class="hero-rule" style="top:187px"></div>
  <h1 class="hero-title" style="top:200px">Bridgeway, Lantern, and the Quiet Harbor Loop</h1>
  <p class="hero-sub" style="top:240px">The Research Program</p>
  <a class="btn" href="#">LEARN MORE</a>
</section>

<svg class="abs" style="left:0;top:600px" width="1200" height="170" viewBox="0 0 1200 170">
  <path d="M0 120 C 200 50, 420 40, 620 80 C 780 110, 860 150, 1000 120 C 1090 100, 1150 75, 1200 55 L1200 170 L0 170Z" fill="#fff"/>
  <path d="M0 112 C 200 42, 420 32, 620 72 C 780 104, 860 140, 1000 112" fill="none" stroke="var(--navy)" stroke-width="9"/>
  <path d="M90 90 C 250 50, 430 48, 620 82 C 780 112, 860 158, 1000 128 C 1090 108, 1150 82, 1200 60" fill="none" stroke="var(--green)" stroke-width="12"/>
</svg>

<section class="vision">
  <div class="venn-circle c-health"></div>
  <div class="venn-circle c-spirit"></div>
  <div class="venn-circle c-values"></div>

  <svg class="venn-icon" style="left:316px;top:800px" width="70" height="70" viewBox="0 0 70 70" fill="none" stroke="#fff" stroke-width="3" stroke-linecap="round" stroke-linejoin="round">
    <path d="M35 40 C 20 30, 18 14, 28 12 C 32 11, 35 15, 35 15 C 35 15, 38 11, 42 12 C 52 14, 50 30, 35 40Z"/>
    <path d="M35 20 v12 M29 26 h12"/>
    <path d="M8 30 v18 l12 14 h8 M62 30 v18 l-12 14 h-8"/>
  </svg>
  <div class="venn-label" style="left:251px;top:878px">Healthcare</div>

  <svg class="venn-icon" style="left:184px;top:1026px" width="70" height="70" viewBox="0 0 70 70" fill="none" stroke="#fff" stroke-width="3" stroke-linecap="round">
    <circle cx="35" cy="20" r="12"/><path d="M35 20 a4 4 0 1 1 4 -4 a8 8 0 1 1 -10 10"/>
    <path d="M8 18 v26 l14 18 M62 18 v26 l-14 18"/>
  </svg>
  <div class="venn-label" style="left:119px;top:1102px">Spiritual Life</div>

  <svg class="venn-icon" style="left:459px;top:1030px" width="70" height="70" viewBox="0 0 70 70" fill="none" stroke="#fff" stroke-width="3" stroke-linecap="round">
    <path d="M26 34 a10 10 0 1 1 18 0 c-3 4,-4 6,-4 10 h-10 c0 -4,-1 -6,-4 -10Z"/><path d="M30 50 h10 M35 4 v4 M22 10 l3 3 M48 10 l-3 3"/>
    <path d="M8 30 v22 l10 12 M62 30 v22 l-10 12 M18 64 h34"/>
  </svg>
  <div class="venn-label" style="left:393px;top:1106px">Values</div>

  <h2 class="vision-title"><b>Vision</b> Statement</h2>
  <p class="vision-text">Lorem ipsum dolor sit amet, consectetur adipiscing elit, sed do eiusmod tempor incididunt ut labore et dolore magna aliqua. Ut enim ad minim veniam, quis nostrud exercitation ullamco laboris nisi ut aliquip ex ea commodo consequat. Duis aute irure dolor in reprehenderit in voluptate velit esse cillum dolore eu fugiat nulla pariatur.</p>
  <a class="btn" href="#">READ MORE</a>
</section>

<section class="program" role="img" aria-label="Aerial view of a dense green forest canopy"></section>
<svg class="abs" style="left:0;top:1285px" width="1200" height="110" viewBox="0 0 1200 110">
  <path d="M0 0 H1200 V15 C 1000 25, 820 40, 600 75 C 400 85, 150 80, 0 45Z" fill="#fff"/>
  <path d="M560 80 C 800 40, 1000 25, 1200 30 L1200 55 C 1000 40, 800 50, 560 80Z" fill="var(--blue-bright)"/>
</svg>
<div class="program-mark"></div>
<h2 class="program-title"><b>Explore our</b> Program</h2>
<article class="card" style="left:111px"><div class="card-photo photo-people" role="img" aria-label="Wind turbines above a sunny meadow with a tree"></div><div class="card-label">People</div></article>
<article class="card" style="left:445px"><div class="card-photo photo-projects" role="img" aria-label="Climber hanging from a rock overhang against a blue sky"></div><div class="card-label">Research Projects</div></article>
<article class="card" style="left:778px"><div class="card-photo photo-faqs" role="img" aria-label="Runner on a tree-lined road at sunset"></div><div class="card-label">FAQs</div></article>

<footer class="site-footer" role="img" aria-label="Blue-tinted mountain lake landscape"></footer>
<svg class="abs" style="left:0;top:1880px" width="1200" height="140" viewBox="0 0 1200 140">
  <path d="M0 140 V120 C 200 60, 420 30, 620 70 C 800 110, 950 120, 1200 40 V140Z" fill="#2a6cab"/>
  <path d="M0 100 C 200 40, 420 10, 620 50 C 800 88, 950 100, 1200 28" fill="none" stroke="var(--blue-bright)" stroke-width="12"/>
  <path d="M0 118 C 200 58, 420 28, 620 68 C 800 106, 950 118, 1200 40" fill="none" stroke="var(--green)" stroke-width="10"/>
</svg>
<div class="footer-mark"></div>
<div class="footer-rule"></div>
<p class="footer-brand">Bridgeway, Lantern, and the Quiet Harbor Loop<br><span style="font-size:15px">The Research Program</span></p>

<h3 class="footer-h" style="left:110px">Quick Links</h3>
<ul class="quick-links">
  <li><svg width="10" height="10" viewBox="0 0 10 10" fill="none" stroke="#fff" stroke-width="1.6"><path d="M1 1l4 4-4 4M5 1l4 4-4 4"/></svg>HOME</li>
  <li><svg width="10" height="10" viewBox="0 0 10 10" fill="none" stroke="#fff" stroke-width="1.6"><path d="M1 1l4 4-4 4M5 1l4 4-4 4"/></svg>PEOPLE</li>
  <li><svg width="10" height="10" viewBox="0 0 10 10" fill="none" stroke="#fff" stroke-width="1.6"><path d="M1 1l4 4-4 4M5 1l4 4-4 4"/></svg>PROJECTS</li>
  <li><svg width="10" height="10" viewBox="0 0 10 10" fill="none" stroke="#fff" stroke-width="1.6"><path d="M1 1l4 4-4 4M5 1l4 4-4 4"/></svg>FAQS</li>
  <li><svg width="10" height="10" viewBox="0 0 10 10" fill="none" stroke="#fff" stroke-width="1.6"><path d="M1 1l4 4-4 4M5 1l4 4-4 4"/></svg>RESOURCES</li>
</ul>

<h3 class="footer-h" style="left:390px;top:2132px">Contact Us</h3>
<ul class="contact-list">
  <li><svg width="12" height="16" viewBox="0 0 12 16"><path d="M6 0a6 6 0 0 1 6 6c0 4-6 10-6 10S0 10 0 6a6 6 0 0 1 6-6z" fill="#fff"/><circle cx="6" cy="6" r="2.2" fill="#2a6cab"/></svg><span>Address:<br>Lorem ipsum dolor sit amet, consectetur<br>adipiscing elit, sed</span></li>
  <li><svg width="14" height="14" viewBox="0 0 14 14"><path d="M3 0l3 3-2 2c1 2 3 4 5 5l2-2 3 3-2 3C6 14 0 8 0 2z" fill="#fff"/></svg><span>Phone :<br>888 - 888 - 8888</span></li>
  <li><svg width="14" height="11" viewBox="0 0 14 11"><rect width="14" height="11" rx="1" fill="#fff"/><path d="M0 1l7 5 7-5" fill="none" stroke="#2a6cab" stroke-width="1.4"/></svg><span>Email :<br>info@quietharborloop.org</span></li>
</ul>

<h3 class="footer-h" style="left:799px;top:2126px">Newsletter</h3>
<p class="newsletter-text">Sed ut perspiciatis unde omnis natus error sit voluptatem</p>
<div class="email-field">Enter Email Id :</div>
<div class="submit">SUBMIT</div>

<div class="footer-divider"></div>
<p class="copyright">© Copyright 2021 Company Name .All Rights Reserved</p>

</body>
</html>
```